Bref créative
Qalvoren Watches - Product Catalogue
Sales and Distribution
Please use some exclusive colours, similar or contrasts in order to support all types of watches’ appear pleasing and easy for eyes.
The catalogue shouldn’t be boring, a well-balanced creativity with a flair of eye-catching theme (people MUST notice it very easy! And most important of all create something that REALLY makes attention).
Miscellaneous
A Bi-Fold Professional Product Catalogue of 6 pages includes the main cover to showcase our distribution brands and latest watch designs.
The outer-side of the main cover and the inner-side should be creatively done with our corporate identity, colour and theme (new ideas and new concepts are encouraged), and inside 4 pages will contain brand name and products.
The catalogue booklet should be handy; should be attractive and industry based as we’re planning to introduce this catalogue in series of editions either monthly or quarterly.
A professionally designed catalogue with graphics & pictures using our identity and presenting us as the professional competent company that we are. This catalogue will be left behind with various resellers, retailers and other corporate groups to keep and hopefully call us when they have orders.
1.Emotional
2. Hi-class
3. Modern
4. Exciting
5. Exclusive
Main action message: "Sales & Distribution”
Further, We want you to use the word “Brand Logo” at the place where you wanted to have the brand names. And please use stock watches at the watch pictures places/positions.
Toll Free No. 9200 48716
website www.qalvorenwatches-example.com
Looking forward to your creativity!
Logo file, ai. version
Dear Designers,
Please let me know, if you find it difficult to open the attached PDF.
Thanks,
TR
Dear designers,
Its just an idea to make something attractive to the minds. But it doesnt mean the catalogue should be designed in the sameway.
Please be creative in your efforts.

```html
<!DOCTYPE html>
<html lang="en">
<head>
<meta charset="utf-8">
<title>Qalvoren Watches – Catalogue Spread</title>
<link rel="stylesheet" href="https://fonts.googleapis.com/css2?family=Arimo:wght@400;700&display=swap">
<style>
  :root{
    --paper:#ffffff;
    --sky:#cfe6f5;
    --sky-deep:#a9d2ee;
    --blue:#1a8fd6;
    --ink:#1f1f1f;
    --soft-ink:#4d5358;
    --steel-light:#f4f6f8;
    --steel-mid:#bfc6cc;
    --steel-dark:#7a838a;
    --fold:#d7dde2;
  }
  *{margin:0;padding:0;box-sizing:border-box}
  html,body{width:1200px;height:775px;overflow:hidden;background:var(--paper)}
  body{font-family:"Arimo",Arial,sans-serif;color:var(--ink)}
  .spread{position:relative;width:1200px;height:775px;overflow:hidden;background:var(--paper)}
  .backdrop{position:absolute;inset:0}
  .fold{position:absolute;left:598px;top:0;width:4px;height:775px;background:var(--fold)}

  .brand-mark{position:absolute;font-weight:700;color:var(--ink)}
  .brand-mark.left{left:30px;top:26px;font-size:24px;letter-spacing:1px}
  .brand-mark.right{right:56px;top:38px;font-size:16px;letter-spacing:2px}

  .product{position:absolute;width:220px;height:196px}
  .product-name{position:absolute;left:0;top:4px;height:96px;writing-mode:vertical-rl;transform:rotate(180deg);
    font-weight:700;font-size:10px;letter-spacing:.3px;color:var(--ink);text-align:left}
  .product-photo{position:absolute;left:52px;top:0;width:130px;height:96px;border-radius:50%;
    background:radial-gradient(ellipse at 50% 50%,var(--steel-light) 0%,var(--steel-mid) 40%,var(--steel-dark) 62%,rgba(255,255,255,0) 72%)}
  .product-photo.gold{background:radial-gradient(ellipse at 50% 50%,#fbf1d8 0%,#d8bd7c 40%,#8a7443 62%,rgba(255,255,255,0) 72%)}
  .product-photo.dark{background:radial-gradient(ellipse at 50% 50%,#c9ced2 0%,#44494e 38%,#1e2226 62%,rgba(255,255,255,0) 72%)}
  .product-photo.blue{background:radial-gradient(ellipse at 50% 50%,#e3ebf5 0%,#4d6c98 40%,#1f2f4e 62%,rgba(255,255,255,0) 72%)}
  .product-photo.pink{background:radial-gradient(ellipse at 50% 50%,#f7e6ea 0%,#c9aab2 40%,#838b92 62%,rgba(255,255,255,0) 72%)}
  .product-desc{position:absolute;left:28px;top:104px;width:178px;font-size:9.5px;line-height:12px;color:var(--soft-ink)}
  .price{position:absolute;left:28px;top:172px;font-weight:700;font-size:14px;color:var(--ink)}

  .page-no{position:absolute;top:350px;width:44px;height:44px;border-radius:50%;background:var(--blue);
    color:var(--paper);font-size:12px;font-weight:700;display:flex;align-items:center}
  .page-no.left{left:-22px;justify-content:flex-end;padding-right:6px}
  .page-no.right{right:-22px;justify-content:flex-start;padding-left:6px}

  .house-mark{position:absolute;top:714px;display:flex;align-items:center;gap:8px;
    font-weight:700;font-size:20px;color:var(--blue)}
  .house-mark .dot{width:26px;height:26px;border-radius:50%;background:var(--blue)}
  .house-mark.left{left:228px}
  .house-mark.right{left:828px}
</style>
</head>
<body>
<main class="spread">
  <svg class="backdrop" width="1200" height="775" viewBox="0 0 1200 775" aria-hidden="true">
    <defs>
      <clipPath id="leftPage"><rect x="0" y="0" width="600" height="775"/></clipPath>
      <clipPath id="rightPage"><rect x="600" y="0" width="600" height="775"/></clipPath>
    </defs>
    <g clip-path="url(#leftPage)">
      <circle cx="560" cy="390" r="470" fill="var(--sky)"/>
      <circle cx="690" cy="390" r="390" fill="var(--paper)"/>
      <circle cx="520" cy="60" r="150" fill="none" stroke="var(--sky-deep)" stroke-width="22" opacity=".6"/>
    </g>
    <g clip-path="url(#rightPage)">
      <circle cx="640" cy="390" r="520" fill="var(--sky)"/>
      <circle cx="560" cy="390" r="430" fill="var(--paper)"/>
      <circle cx="700" cy="700" r="170" fill="none" stroke="var(--sky-deep)" stroke-width="22" opacity=".6"/>
    </g>
  </svg>
  <div class="fold"></div>

  <div class="brand-mark left">VELTARO</div>
  <div class="brand-mark right">NORRIVEL</div>

  <!-- left page -->
  <section class="product" style="left:30px;top:92px">
    <div class="product-name">PRODUCT NAME</div>
    <div class="product-photo" role="img" aria-label="Silver steel wristwatch with square dial"></div>
    <p class="product-desc">Product description Product description Product description Product description Product description Product description Product description Product description Product description</p>
    <div class="price">$ 00000</div>
  </section>
  <section class="product" style="left:338px;top:92px">
    <div class="product-name">PRODUCT NAME</div>
    <div class="product-photo" role="img" aria-label="Steel diver wristwatch"></div>
    <p class="product-desc">Product description Product description Product description Product description Product description Product description Product description Product description Product description</p>
    <div class="price">$ 00000</div>
  </section>
  <section class="product" style="left:30px;top:298px">
    <div class="product-name">PRODUCT NAME</div>
    <div class="product-photo pink" role="img" aria-label="Steel bracelet watch with pink dial"></div>
    <p class="product-desc">Product description Product description Product description Product description Product description Product description Product description Product description Product description</p>
    <div class="price">$ 00000</div>
  </section>
  <section class="product" style="left:338px;top:298px">
    <div class="product-name">PRODUCT NAME</div>
    <div class="product-photo" role="img" aria-label="Square steel bracelet watch"></div>
    <p class="product-desc">Product description Product description Product description Product description Product description Product description Product description Product description Product description</p>
    <div class="price">$ 00000</div>
  </section>
  <section class="product" style="left:30px;top:502px">
    <div class="product-name">PRODUCT NAME</div>
    <div class="product-photo gold" role="img" aria-label="Gold watch with leather strap"></div>
    <p class="product-desc">Product description Product description Product description Product description Product description Product description Product description Product description Product description</p>
    <div class="price">$ 00000</div>
  </section>
  <section class="product" style="left:338px;top:502px">
    <div class="product-name">PRODUCT NAME</div>
    <div class="product-photo" role="img" aria-label="Steel sports watch on bracelet"></div>
    <p class="product-desc">Product description Product description Product description Product description Product description Product description Product description Product description Product description</p>
    <div class="price">$ 00000</div>
  </section>

  <!-- right page -->
  <section class="product" style="left:648px;top:92px">
    <div class="product-name">PRODUCT NAME</div>
    <div class="product-photo gold" role="img" aria-label="Two-tone chronograph watch"></div>
    <p class="product-desc">Product description Product description Product description Product description Product description Product description Product description Product description Product description</p>
    <div class="price">$ 00000</div>
  </section>
  <section class="product" style="left:938px;top:92px">
    <div class="product-name">PRODUCT NAME</div>
    <div class="product-photo blue" role="img" aria-label="Blue dial chronograph on strap"></div>
    <p class="product-desc">Product description Product description Product description Product description Product description Product description Product description Product description Product description</p>
    <div class="price">$ 00000</div>
  </section>
  <section class="product" style="left:648px;top:298px">
    <div class="product-name">PRODUCT NAME</div>
    <div class="product-photo dark" role="img" aria-label="Black dial chronograph watch"></div>
    <p class="product-desc">Product description Product description Product description Product description Product description Product description Product description Product description Product description</p>
    <div class="price">$ 00000</div>
  </section>
  <section class="product" style="left:938px;top:298px">
    <div class="product-name">PRODUCT NAME</div>
    <div class="product-photo" role="img" aria-label="Steel chronograph with white dial"></div>
    <p class="product-desc">Product description Product description Product description Product description Product description Product description Product description Product description Product description</p>
    <div class="price">$ 00000</div>
  </section>
  <section class="product" style="left:648px;top:502px">
    <div class="product-name">PRODUCT NAME</div>
    <div class="product-photo" role="img" aria-label="Steel pilot chronograph"></div>
    <p class="product-desc">Product description Product description Product description Product description Product description Product description Product description Product description Product description</p>
    <div class="price">$ 00000</div>
  </section>
  <section class="product" style="left:938px;top:502px">
    <div class="product-name">PRODUCT NAME</div>
    <div class="product-photo gold" role="img" aria-label="Gold chronograph on bracelet"></div>
    <p class="product-desc">Product description Product description Product description Product description Product description Product description Product description Product description Product description</p>
    <div class="price">$ 00000</div>
  </section>

  <div class="page-no left">01</div>
  <div class="page-no right">02</div>

  <div class="house-mark left"><span class="dot"></span>Qalvoren Watches</div>
  <div class="house-mark right"><span class="dot"></span>Qalvoren Watches</div>
</main>
</body>
</html>
```